BELU Safety Poster

We need a safety poster designed that we can provide to our members to put up on the wall of their factories. It needs to be clear and concise and simple but also that they are aware it is provided by us. We would like the poster to be in line with our branding companies, you can view these on our website www.tarnvalehub.com A3 size please

All files are here https://www.quillstash.com/sh/p8ve2mz7tqs4lr9/QQhuTrwc-LPMaxRuF83Zcf5H1?n=47193052

```html
<!DOCTYPE html>
<html lang="en">
<head>
<meta charset="utf-8">
<title>BELU Safety Poster – Heat Stress</title>
<link href="https://fonts.googleapis.com/css2?family=Archivo+Black&family=Courier+Prime:wght@700&family=Archivo:wght@400;800&display=swap" rel="stylesheet">
<style>
  :root{
    --backdrop:#e9e9e7;
    --hazard-yellow:#e0a51c;
    --hazard-black:#111111;
    --panel-orange:#f0a21a;
    --panel-glow:#fff200;
    --ink:#0d0d0d;
    --cone-cream:#f3dfa0;
    --hat-orange:#e8731c;
  }
  *{box-sizing:border-box;margin:0;padding:0}
  html,body{width:1200px;height:1000px;overflow:hidden}
  body{background:var(--backdrop);position:relative;font-family:"Archivo",Arial,sans-serif;color:var(--ink)}

  .poster{
    position:absolute;left:40px;top:94px;width:1120px;height:812px;
    background:repeating-linear-gradient(135deg,
      var(--hazard-black) 0 14px,var(--hazard-yellow) 14px 40px);
  }
  .poster__panel{
    position:absolute;left:26px;top:24px;right:26px;bottom:24px;
    border-radius:22px;
    background:radial-gradient(ellipse 360px 300px at 524px 324px,var(--panel-glow) 0%,#ffd20a 35%,var(--panel-orange) 80%);
  }
  .poster__title{
    position:absolute;left:0;right:0;top:40px;text-align:center;
    font-family:"Archivo Black",Arial,sans-serif;font-size:68px;letter-spacing:-2.5px;line-height:1;
  }
  .poster__hero{
    position:absolute;left:445px;top:146px;width:172px;height:356px;
    border-radius:60px 60px 20px 20px;
    background:linear-gradient(180deg,var(--hat-orange) 0 24%,var(--cone-cream) 24% 100%);
  }
  .tips{
    position:absolute;left:0;right:0;top:532px;text-align:center;
    font-family:"Courier Prime","Courier New",monospace;font-weight:700;font-size:19.5px;line-height:28px;
  }
  .tips__sep{display:inline-block;width:15px;height:15px;background:var(--ink);vertical-align:-1px;margin:0 2px}
  .signs{position:absolute;left:31px;top:598px}
  .signs__heading{font-family:"Archivo",Arial,sans-serif;font-weight:800;font-size:17px;margin-bottom:6px}
  .signs__list{list-style:none;font-family:"Courier Prime","Courier New",monospace;font-weight:700;font-size:21px;line-height:25px}
  .footnote{position:absolute;left:31px;top:722px;font-size:9.5px;line-height:12px;width:420px}
  .provider{position:absolute;left:850px;top:618px}
  .provider__line1{font-weight:800;font-size:15px;line-height:17px}
  .provider__line2{font-weight:400;font-size:17px;line-height:19px;letter-spacing:-.3px}
  .provider__brand{display:flex;align-items:center;gap:8px;margin-top:18px}
  .provider__dot{width:34px;height:34px;border-radius:50%;background:var(--ink)}
  .provider__name{font-weight:400;font-size:12px;line-height:13px;width:110px}
</style>
</head>
<body>
  <section class="poster" aria-label="BELU heat stress safety poster">
    <div class="poster__panel">
      <h1 class="poster__title">HEAT STRESS ISN'T COOL</h1>
      <div class="poster__hero" role="img" aria-label="Melting ice cream cone wearing an orange hard hat"></div>

      <p class="tips">DRINK PLENTY OF WATER<span class="tips__sep"></span>TAKE BREAKS<span class="tips__sep"></span>WEAR LIGHT CLOTHING WHEN APPROPRIATE<br>MONITOR WORK MATES FOR SIGNS OF HEAT STRESS</p>

      <div class="signs">
        <h2 class="signs__heading">SIGNS OF HEAT STRESS OR HEAT EXHAUSTION</h2>
        <ul class="signs__list">
          <li>FEELING SICK, WEAK OR CLUMSY / DIZZY.</li>
          <li>CRAMPS CAN ALSO BE CAUSED BY HEAT</li>
          <li>DISCOMFORT FROM HEAT RASH</li>
        </ul>
      </div>

      <p class="footnote">** If you have profuse sweating, weakness, nausea or vomiting, headaches and muscle spasms then stop work immediately and seek help.</p>

      <div class="provider">
        <p class="provider__line1">THIS IS AN BELU</p>
        <p class="provider__line2">SAFETY POSTER</p>
        <div class="provider__brand">
          <span class="provider__dot"></span>
          <span class="provider__name">Tarnvale Moulders Guild</span>
        </div>
      </div>
    </div>
  </section>
</body>
</html>
```